Dodgeball League website

I require a nice, cool and attractive website for a new dodgeball league competition. I will need in PSD:

- Home Page
- Generic pages for news, about us etc
- Rank page with a table of team scores. stats etc

*Please design this with a Joomla*

I have attached:
- a logo
- site map for the links
- page layout guide

Example site for layout
http://www.velmorcircuit.com/

Design
Retro,cool feel, matches well with logo

Contact me if you have any questions

Reason: Would like to see a few more designs

Target Market(s)

Young adults 18 - 35.

Industry/Entity Type

News

Colors

Designer to choose colors to be used in the design.

Requirements
Must have
• I want a cool, retro feel to the website. Not to picky on the colors. Something that will match nicely with the logo given. I will give feedback on it.
Calm colors not too bright and overwhelming
Nice to have
• Include some pictures within the picture slider so I can get a feel for the website.
Nice clean background
Should not have
• To much clutter of text
Do not put pictures in the background.

```html
<!DOCTYPE html>
<html lang="en">
<head>
<meta charset="utf-8">
<title>Harbour Dodge League</title>
<link href="https://fonts.googleapis.com/css2?family=Signika:wght@400;600;700&family=Open+Sans:wght@400;600;700&display=swap" rel="stylesheet">
<style>
:root{
  --orange:#e2531b;
  --orange-dark:#c8410f;
  --yellow:#fcc824;
  --yellow-soft:#fde27a;
  --bg:#f4ede6;
  --ink:#222;
  --muted:#777;
  --navy:#2b3a8c;
  --white:#fff;
}
*{box-sizing:border-box;margin:0;padding:0}
html,body{width:1010px;height:1200px;overflow:hidden}
body{position:relative;background:repeating-linear-gradient(90deg,var(--bg) 0 3px,#f0e8e0 3px 4px);font-family:'Open Sans',sans-serif;color:var(--ink)}
.abs{position:absolute}
.header{left:0;top:0;width:1010px;height:86px;background:var(--white)}
.brand{left:160px;top:16px;height:56px;z-index:3;display:flex;align-items:center;gap:8px}
.brand-dot{width:50px;height:50px;border-radius:50%;background:var(--yellow);border:4px solid var(--orange);flex:none}
.brand-name{font-family:'Signika',sans-serif;font-weight:700;font-size:16px;color:var(--orange);line-height:1.05}
.score{top:22px;width:130px;height:55px;font-family:'Signika',sans-serif;font-size:9px;box-shadow:0 1px 3px rgba(0,0,0,.3)}
.score .head{height:17px;background:#111;color:#fff;display:flex;justify-content:space-between;padding:0 7px;align-items:center;font-weight:600}
.score .row{height:19px;display:flex;justify-content:space-between;padding:0 10px 0 8px;align-items:center;color:#fff;font-size:7.5px;font-weight:600}
.score.a .row{background:var(--orange)}
.score.b .row{background:var(--yellow)}
.score .row b{color:var(--yellow)}
.score.b .row b{color:var(--orange)}
.pole{width:4px;height:12px;background:#bbb;top:77px}
.nav{left:0;top:86px;width:1010px;height:36px;background:linear-gradient(var(--orange),var(--orange-dark))}
.nav ul{position:absolute;left:268px;top:0;height:36px;display:flex;gap:13px;list-style:none;align-items:center}
.nav li{font-family:'Signika',sans-serif;font-weight:700;font-size:9.5px;color:#fff}
.search{left:722px;top:93px;width:120px;height:22px;border-radius:11px;background:#fff;font-size:8px;color:#aaa;padding:6px 12px;overflow:hidden}
.search-btn{left:814px;top:93px;width:28px;height:22px;border-radius:0 11px 11px 0;background:var(--orange-dark)}
.hero{left:0;top:122px;width:1010px;height:302px;background:linear-gradient(180deg,#9c8a70 0%,#3c4f8c 35%,#b58a5a 60%,#d9b792 100%)}
.hero-shadow{left:20px;top:424px;width:970px;height:14px;background:radial-gradient(ellipse at top,rgba(0,0,0,.25),transparent 70%)}
.caption{left:170px;top:356px;width:446px;height:68px;background:linear-gradient(90deg,rgba(214,72,20,.95),rgba(226,83,27,.8));clip-path:polygon(0 0,100% 0,88% 100%,0 100%);color:#fff;padding:6px 24px}
.caption h1{font-family:'Signika',sans-serif;font-weight:400;font-size:28px;letter-spacing:-1px;line-height:1.1}
.caption p{font-size:8.5px;margin-top:1px}
.caption a{display:block;font-size:8.5px;font-weight:700;margin-top:2px}
.dots{left:513px;top:409px;display:flex;gap:3px}
.dots i{width:8px;height:8px;border-radius:50%;background:#fff}
.dots i:first-child{background:var(--yellow)}
.card{background:#fff;border-radius:4px;box-shadow:0 1px 3px rgba(0,0,0,.15)}
.news{left:170px;top:458px;width:426px;height:196px}
.news h2{position:absolute;left:15px;top:6px;font-family:'Signika',sans-serif;font-weight:700;font-size:20px;color:var(--orange)}
.news .rule{position:absolute;left:138px;top:20px;width:200px;border-top:1px dotted #ccc}
.arrows{position:absolute;left:378px;top:12px;display:flex;gap:3px}
.arrows i{width:16px;height:16px;border-radius:50%;background:var(--orange-dark)}
.news .bar{position:absolute;left:0;top:36px;width:426px;height:5px;background:var(--yellow)}
.news-photo{position:absolute;left:16px;top:54px;width:128px;height:126px;border:4px solid #fff;box-shadow:0 0 3px rgba(0,0,0,.3);background:linear-gradient(#4d6a3a,#7a8e52 50%,#3e5a2c)}
.news-body{position:absolute;left:157px;top:52px;width:250px}
.news-date{font-family:'Signika',sans-serif;font-weight:700;font-size:15px;color:var(--navy)}
.news-title{font-family:'Signika',sans-serif;font-weight:600;font-size:17px;color:var(--orange);line-height:1.2}
.news-text{font-size:7.3px;color:var(--muted);line-height:1.42;margin-top:2px}
.news-more{font-size:7.5px;font-weight:700;color:var(--orange);margin-top:5px}
.like{left:606px;top:458px;width:244px;height:92px;background:linear-gradient(110deg,#fff 0 30%,#fbd3b8 30% 55%,#fff 55% 70%,#f8c6a6 70%)}
.like-title{position:absolute;left:8px;top:8px;font-family:'Signika',sans-serif;font-weight:700;font-size:30px;color:var(--orange);letter-spacing:-2px;line-height:1}
.like-sub{position:absolute;left:12px;top:40px;font-family:'Signika',sans-serif;font-weight:700;font-size:19px;color:var(--orange)}
.like-sub span{color:var(--navy)}
.like-note{position:absolute;left:36px;top:64px;font-size:7px;color:var(--orange);line-height:1.3}
.like-brand{position:absolute;left:160px;top:10px;width:80px;height:74px;display:flex;flex-direction:column;align-items:center}
.like-brand i{width:46px;height:46px;border-radius:50%;background:var(--yellow);border:3px solid var(--orange)}
.like-brand span{font-family:'Signika',sans-serif;font-weight:700;font-size:10px;color:var(--orange);text-align:center;line-height:1.05}
.reg{left:606px;top:562px;width:244px;height:92px}
.box-title{position:absolute;left:12px;top:4px;font-family:'Signika',sans-serif;font-weight:700;font-size:13px;color:var(--orange);display:flex;align-items:center;gap:5px}
.box-bar{position:absolute;left:0;top:24px;width:100%;height:4px;background:var(--yellow)}
.field{position:absolute;height:19px;border:1px solid #ccc;border-radius:10px;font-size:7.5px;color:#aaa;padding:4px 16px;background:#fff}
.reg-btn{position:absolute;left:160px;top:62px;width:70px;height:19px;border-radius:10px;background:#e03328;color:#fff;font-size:7.5px;font-weight:700;text-align:center;line-height:19px}
.league{left:170px;top:664px;width:426px;height:312px;background:var(--orange-dark);border-radius:4px}
.tab-a{position:absolute;left:0;top:0;width:230px;height:40px;color:#fff;font-family:'Signika',sans-serif;font-weight:600;font-size:14px;padding:12px 14px;letter-spacing:-.5px}
.tab-b{position:absolute;left:212px;top:0;width:214px;height:38px;background:var(--yellow);clip-path:polygon(0 0,100% 0,100% 100%,8% 100%);color:#fff;font-family:'Signika',sans-serif;font-weight:600;font-size:14px;padding:10px 0 0 34px;letter-spacing:-.5px}
.ranks{position:absolute;left:9px;top:42px;width:409px;border-collapse:collapse;font-family:'Signika',sans-serif}
.ranks th{height:38px;background:var(--yellow);color:var(--orange);font-weight:600;font-size:12px;letter-spacing:-.5px}
.ranks td{height:28px;font-size:12px;color:var(--orange);background:#fff}
.ranks tr:nth-child(even) td{background:#e9e9e9}
.ranks td:first-child,.ranks th:first-child{width:88px;text-align:center;border-right:1px solid #ddd}
.ranks td:nth-child(2),.ranks th:nth-child(2){text-align:left;padding-left:13px;border-right:1px solid #ddd}
.ranks td:nth-child(2){color:#222;font-size:8.5px;font-weight:600;letter-spacing:-.4px}
.ranks td:last-child,.ranks th:last-child{width:86px;text-align:center}
.fb{left:606px;top:666px;width:244px;height:212px}
.fb-head{position:absolute;left:0;top:0;width:100%;height:24px;background:#eceef3;font-size:9px;font-weight:700;color:#333;padding:6px 5px}
.fb-logo{position:absolute;left:8px;top:32px;width:40px;height:40px;border-radius:50%;background:var(--yellow);border:2px solid var(--orange)}
.fb-name{position:absolute;left:56px;top:32px;font-size:9px;color:#ddd}
.fb-btn{position:absolute;left:54px;top:50px;width:46px;height:16px;border:1px solid #99a;border-radius:2px;font-size:8px;color:#3b5998;text-align:center;line-height:14px;background:#f4f5f8}
.fb-count{position:absolute;left:8px;top:84px;font-size:8px;color:#333}
.fb-grid{position:absolute;left:8px;top:102px;display:grid;grid-template-columns:repeat(5,42px);gap:2px 2px}
.fb-grid i{height:41px}
.fb-foot{position:absolute;left:8px;top:192px;font-size:7px;color:#777}
.loc{left:606px;top:890px;width:244px;height:86px}
.map{position:absolute;left:0;top:28px;width:244px;height:58px;background:linear-gradient(135deg,#efe9dc,#f6e3a0 60%,#ece6d8)}
.top3{top:1010px;width:222px;height:86px;background:linear-gradient(var(--yellow),#f0a91b);border-radius:4px;border:2px solid #e8961a}
.players{position:absolute;left:-8px;top:-24px;width:120px;height:108px;background:linear-gradient(#c99a7a 0 25%,#2b3c78 25% 60%,#1e1e1e 60%)}
.top3-info{position:absolute;left:116px;top:6px;font-family:'Signika',sans-serif;font-size:9.5px;color:#222;line-height:1.4}
.top3-info h3{font-size:19px;font-weight:600;color:#e03328;letter-spacing:-1px;line-height:1;margin-bottom:2px}
.top3-info em{font-style:normal;color:#e03328}
.partners{left:0;top:1114px;width:1010px;height:43px;background:#f7f6f4;display:flex;justify-content:center;align-items:center;gap:38px}
.partners i{width:70px;height:18px;border-radius:3px;background:#bdbdbd}
.footer{left:0;top:1157px;width:1010px;height:43px;background:var(--orange-dark);display:flex;justify-content:center;align-items:center;gap:8px;color:#fde2cf;font-size:10px}
.footer i{width:30px;height:30px;border-radius:50%;background:var(--yellow);border:2px solid #fff}
</style>
</head>
<body>
<div class="abs header"></div>
<div class="abs brand"><div class="brand-dot"></div><div class="brand-name">Harbour Dodge<br>League</div></div>

<div class="abs pole" style="left:606px"></div><div class="abs pole" style="left:690px"></div>
<div class="abs pole" style="left:740px"></div><div class="abs pole" style="left:824px"></div>
<div class="abs score a" style="left:584px"><div class="head"><span>Team</span><span>Score</span></div><div class="row"><span><b>01:</b> Hit Runners</span><span>10</span></div><div class="row"><span><b>02:</b> But Smarter</span><span>05</span></div></div>
<div class="abs score b" style="left:718px"><div class="head"><span>Team</span><span>Score</span></div><div class="row"><span><b>03:</b> Hit Runners</span><span>10</span></div><div class="row"><span><b>04:</b> But Smarter</span><span>05</span></div></div>

<nav class="abs nav"><ul><li>HOME</li><li>ABOUT</li><li>TEAMS</li><li>SCHEDULE</li><li>NEWS</li><li>PHOTO AND VIDEOS</li><li>REGISTER</li><li>CONTACT US</li></ul></nav>
<div class="abs search">Search....</div>
<div class="abs search-btn"><svg width="28" height="22" viewBox="0 0 28 22"><path d="M8 6l5 5-5 5M14 6l5 5-5 5" stroke="#fcc824" stroke-width="2.5" fill="none"/></svg></div>

<div class="abs hero" role="img" aria-label="Dodgeball players lunging for balls on an indoor court with spectators"></div>
<div class="abs hero-shadow"></div>
<div class="abs caption"><h1>Marlow Holds Off Vance</h1><p>Rafe Marlow sets a contest with Final Showdown contender Tobias Kelder in Paris.</p><a>&raquo; Read More &amp; Watch Highlights</a></div>
<div class="abs dots"><i></i><i></i><i></i><i></i><i></i></div>

<section class="abs card news">
  <h2>Latest News</h2><div class="rule"></div>
  <div class="arrows"><i></i><i></i></div>
  <div class="bar"></div>
  <div class="news-photo" role="img" aria-label="Team group photo holding dodgeballs on grass"></div>
  <div class="news-body">
    <div class="news-date">28.JULY.2013</div>
    <div class="news-title">Hollis On Brink Of Qualifying</div>
    <p class="news-text">Lorem ipsum dolor sit amet, consectetuer adipiscing elit, sed diam nonummy nibh euismod tincidunt ut laoreet dolore magna aliquam erat volutpat. Ut wisi enim ad minim veniam, quis nostrud exerci tation ullamcorper suscipit lobortis nisl ut aliquip ex ea commodo consequat. Duis autem vel eum iriure dolor in hendrerit in vulputate velit esse molestie consequat, vel illum dolore eu feugiat nulla facilisis at vero pit lobortis nisl ut aliquip pit lobortis nisl ut aliquip</p>
    <div class="news-more">READ MORE &gt;&gt;</div>
  </div>
</section>

<aside class="abs card like">
  <div class="like-title">“LIKE US”</div>
  <div class="like-sub">On <span>Circlebook</span></div>
  <div class="like-note">Lorem Ipsum Dolor Sit<br>Ex Ea Commodo Consequ.</div>
  <div class="like-brand"><i></i><span>Harbour Dodge<br>League</span></div>
</aside>

<aside class="abs card reg">
  <div class="box-title"><svg width="11" height="13"><rect x="1" y="1" width="9" height="11" fill="none" stroke="#333"/><path d="M3 4h5M3 6.5h5M3 9h5" stroke="#333"/></svg>Registerd Now</div>
  <div class="box-bar"></div>
  <div class="field" style="left:12px;top:37px;width:220px">Email Adderess.......</div>
  <div class="field" style="left:12px;top:62px;width:144px">Name.......</div>
  <div class="reg-btn">Registerd Now</div>
</aside>

<section class="abs league">
  <div class="tab-a">Ultimate Rubber League</div>
  <div class="tab-b">Ultimate Foam League</div>
  <table class="ranks">
    <tr><th>Team Rank</th><th>Team Name</th><th>Score</th></tr>
    <tr><td>01</td><td>HIT RUNNERS</td><td>25</td></tr>
    <tr><td>02</td><td>BEAUTIES &amp; THE BEAST</td><td>21</td></tr>
    <tr><td>03</td><td>CHICKS &amp; AN OLD GUY</td><td>19</td></tr>
    <tr><td>04</td><td>FAST 1 FURIOUS</td><td>17</td></tr>
    <tr><td>05</td><td>OR BUST</td><td>14</td></tr>
    <tr><td>06</td><td>SHADES OF RUNNING</td><td>12</td></tr>
    <tr><td>07</td><td>BUT SMARTER</td><td>11</td></tr>
    <tr><td>08</td><td>21K TO VEGAS</td><td>09</td></tr>
  </table>
</section>

<aside class="abs card fb">
  <div class="fb-head">Find us on Circlebook</div>
  <div class="fb-logo"></div>
  <div class="fb-name">Harbour Dodge League</div>
  <div class="fb-btn">Like</div>
  <div class="fb-count">2,237,773 people like Harbour Dodge</div>
  <div class="fb-grid" role="img" aria-label="Grid of follower profile photos"><i style="background:#8a8a8a"></i><i style="background:#b08e7a"></i><i style="background:#6f7f5a"></i><i style="background:#5e7a4a"></i><i style="background:#7a5a44"></i><i style="background:#9a9a9a"></i><i style="background:#4a6a2a"></i><i style="background:#6a8a2a"></i><i style="background:#7a8a6a"></i><i style="background:#3a2a1a"></i></div>
  <div class="fb-foot">Circlebook social plugin</div>
</aside>

<aside class="abs card loc">
  <div class="box-title"><svg width="11" height="14"><path d="M5.5 13C2 8 1 6.5 1 5a4.5 4.5 0 019 0c0 1.5-1 3-4.5 8z" fill="none" stroke="#333" stroke-width="1.4"/><circle cx="5.5" cy="5" r="1.6" fill="#333"/></svg>Find Your Location</div>
  <div class="box-bar"></div>
  <div class="map" role="img" aria-label="Street map of the league venue area"></div>
</aside>

<div class="abs top3" style="left:170px"><div class="players" role="img" aria-label="Three players in team jerseys"></div><div class="top3-info"><h3>Top 3 Killers</h3><em>Team</em> : Shades &amp; orbust<br><em>Score</em> : 25 &nbsp; <em>Rank</em> : 02<br><em>Names</em> :<br>Brain, Abrian, Dayer</div></div>
<div class="abs top3" style="left:398px"><div class="players" role="img" aria-label="Three players in team jerseys"></div><div class="top3-info"><h3>Top 3 catcher</h3><em>Team</em> : Shades &amp; orbust<br><em>Score</em> : 25 &nbsp; <em>Rank</em> : 02<br><em>Names</em> :<br>Brain, Abrian, Dayer</div></div>
<div class="abs top3" style="left:627px"><div class="players" role="img" aria-label="Three players in team jerseys"></div><div class="top3-info"><h3>Top 3 Dodger</h3><em>Team</em> : Shades &amp; orbust<br><em>Score</em> : 25 &nbsp; <em>Rank</em> : 02<br><em>Names</em> :<br>Brain, Abrian, Dayer</div></div>

<div class="abs partners"><i></i><i></i><i></i><i></i><i></i><i></i></div>
<footer class="abs footer"><i></i>Copyright © 2013 HarbourDodgeLeague. All Rights Reserved.</footer>
</body>
</html>
```